Law Firm Stationery Design - Traditional Meets Intuitive

Looking for a modern, yet classic, law firm stationery design. Simplicity is desired, but great ideas are encouraged. See attachment for company information. We utilize a variety of non-traditional legal tools to bring a different perspective to each of our client's particular situation. Final design should communicate classic values with intuitive, unique solutions.

Industry/Entity Type

Law Firm

Requirements
Should not have
• - No typical legal icons
• - No Tag Line!
• - DO NOT WANT WHAT WE ALREADY HAVE

```html
<!DOCTYPE html>
<html lang="en">
<head>
<meta charset="UTF-8">
<title>Verant Law – Business Card</title>
<link rel="stylesheet" href="https://fonts.googleapis.com/css2?family=Libre+Baskerville&family=Open+Sans:wght@400;600&display=swap">
<style>
  :root {
    --page-bg: #e8e5e0;
    --band-dark: #141414;
    --band-dark-2: #2a2a2a;
    --frost-1: #f3f1ee;
    --frost-2: #dcdad6;
    --ink: #1b1b1b;
    --band-blue: #1b3a63;
    --band-blue-2: #2f5f95;
    --name-light: #e4e4e4;
    --title-muted: #b9ada0;
    --firm-gold: #cfae72;
    --contact-light: #dfe6ef;
  }
  * { margin: 0; padding: 0; box-sizing: border-box; }
  html, body {
    width: 1200px; height: 969px; overflow: hidden;
    background: var(--page-bg);
  }
  .card {
    position: absolute; left: 100px; top: 200px;
    width: 1000px; height: 569px;
    box-shadow: 0 18px 40px rgba(0,0,0,0.18);
    overflow: hidden;
    font-family: "Open Sans", Arial, sans-serif;
  }
  .card__header {
    height: 125px;
    background: linear-gradient(180deg, var(--band-dark-2), var(--band-dark));
    display: flex; align-items: center; justify-content: center;
    gap: 12px;
    padding-left: 60px;
  }
  .card__name {
    color: var(--name-light); font-size: 32px; letter-spacing: 1px;
  }
  .card__role {
    color: var(--title-muted); font-size: 26px;
  }
  .card__body {
    height: 284px;
    background: radial-gradient(ellipse at 50% 40%, var(--frost-1), var(--frost-2));
    display: flex; align-items: center; justify-content: center;
  }
  .card__firm {
    font-family: "Libre Baskerville", Georgia, serif;
    font-size: 84px; color: var(--ink); line-height: 1.1;
  }
  .card__footer {
    height: 160px;
    background: linear-gradient(180deg, var(--band-blue-2), var(--band-blue));
    display: flex; justify-content: space-between; align-items: center;
    padding: 0 54px 0 70px;
    color: var(--contact-light);
    font-size: 26px;
  }
  .contact-list { list-style: none; }
  .contact-list li {
    display: flex; align-items: center; gap: 14px; height: 38px;
  }
  .contact-list svg { width: 22px; height: 22px; fill: none; stroke: var(--contact-light); stroke-width: 2; }
  .address { text-align: right; line-height: 38px; }
  .address__firm { color: var(--firm-gold); font-weight: 600; letter-spacing: 0.5px; }
</style>
</head>
<body>
  <div class="card">
    <header class="card__header">
      <span class="card__name">DANIEL REYES</span>
      <span class="card__role">- CEO/Founder</span>
    </header>
    <section class="card__body">
      <div class="card__firm">Verant Law</div>
    </section>
    <footer class="card__footer">
      <ul class="contact-list">
        <li>
          <svg viewBox="0 0 22 22" aria-hidden="true"><rect x="6" y="2" width="10" height="18" rx="2"/><line x1="10" y1="17" x2="12" y2="17"/></svg>
          <span>555-014-2800</span>
        </li>
        <li>
          <svg viewBox="0 0 22 22" aria-hidden="true"><rect x="2" y="5" width="18" height="12"/><polyline points="2,5 11,12 20,5"/></svg>
          <span>info@verantlaw.com</span>
        </li>
        <li>
          <svg viewBox="0 0 22 22" aria-hidden="true"><circle cx="11" cy="11" r="8"/><ellipse cx="11" cy="11" rx="3.5" ry="8"/><line x1="3" y1="11" x2="19" y2="11"/></svg>
          <span>www.verantlaw.com</span>
        </li>
      </ul>
      <div class="address">
        <div class="address__firm">VERANT LAW LLC</div>
        <div>18 Harbor Lane, Suite 300</div>
        <div>Easton, CT 06612</div>
      </div>
    </footer>
  </div>
</body>
</html>
```